Pediatric Speech Therapy Private Practice Announcement

I opened a solo private practice as a pediatric speech therapist in June 2014 in Orinda, CA in June 2014. I have 25 years experience in the field and worked as the Director of a very successful group practice of speech therapists in nearby Walnut Creek. I am trying to get my own name established in the local community and letting people know that I now have my own practice, which I call Halvery Speech-Language Center.

I would like this postcard to advertise low-cost speech-language screenings offered to nearby preschools.

Target Market(s)

Preschool Directors

Industry/Entity Type

Call

Requirements
Must have
• Photos of children, preschool ages, 3-5

Bright colors to get attention

```html
<!DOCTYPE html>
<html lang="en">
<head>
<meta charset="utf-8">
<title>Halvery Speech-Language Center – Preschool Screening Postcard</title>
<link href="https://fonts.googleapis.com/css2?family=Jost:wght@400;500&family=Questrial&display=swap" rel="stylesheet">
<style>
  :root {
    --stage: #4a4a4a;
    --paper: #ffffff;
    --sun: #ffd21f;
    --sun-soft: #fff4b8;
    --teal: #1b6b8c;
    --magenta: #e0197d;
    --orange: #f07a1e;
    --navy: #1d2a5c;
    --band-text-yellow: #fff200;
    --frame-edge: #cfcfcf;
  }
  * { box-sizing: border-box; margin: 0; padding: 0; }
  html, body { width: 1200px; height: 815px; overflow: hidden; }
  body { background: var(--stage); position: relative; font-family: "Jost", sans-serif; }

  .postcard {
    position: absolute; left: 60px; top: 60px; width: 1080px; height: 695px;
    overflow: hidden;
    background: linear-gradient(90deg, var(--paper) 0%, var(--paper) 42%, var(--sun-soft) 64%, var(--sun) 100%);
  }

  .headline {
    position: absolute; left: 42px; top: 36px; z-index: 3;
    font-family: "Jost", sans-serif; font-weight: 400; font-size: 50px; line-height: 53px;
    color: var(--teal); white-space: nowrap;
  }
  .headline .accent { color: var(--magenta); }

  .group-photo {
    position: absolute; left: 10px; top: 105px; width: 475px; height: 450px; z-index: 1;
    border-radius: 50%;
    background: radial-gradient(circle at 50% 50%, #c9e07a 0%, #f2b9c6 35%, #e9cfb6 60%, rgba(255,255,255,0) 72%);
  }

  .intro {
    position: absolute; left: 417px; top: 180px; z-index: 3;
    font-size: 17px; line-height: 23px; color: var(--navy); white-space: nowrap;
  }

  .call-block {
    position: absolute; left: 475px; top: 352px; width: 300px; z-index: 3;
    text-align: center; font-family: "Questrial", sans-serif; white-space: nowrap;
  }
  .call-today { color: var(--orange); font-size: 29px; line-height: 36px; }
  .phone { color: var(--magenta); font-size: 38px; line-height: 48px; margin-top: 4px; }
  .call-note { color: var(--navy); font-size: 17px; line-height: 21px; margin-top: 8px; }
  .call-note .highlight { color: var(--magenta); }

  .website {
    position: absolute; left: 307px; top: 529px; z-index: 3;
    font-family: "Questrial", sans-serif; font-size: 19px; color: var(--magenta);
  }

  .brand-band {
    position: absolute; left: 0; top: 568px; width: 1080px; height: 105px; z-index: 2;
    background: var(--magenta); padding: 18px 0 0 52px;
    font-family: "Questrial", sans-serif; white-space: nowrap;
  }
  .brand-name { color: #fff; font-size: 40px; line-height: 44px; }
  .brand-services { color: var(--band-text-yellow); font-size: 25px; line-height: 32px; margin-top: 2px; }

  .snapshot {
    position: absolute; z-index: 4; background: #fff; padding: 11px;
    border: 1px solid var(--frame-edge);
  }
  .snapshot .photo { width: 100%; height: 100%; }
  .snapshot--classroom { left: 862px; top: -8px; width: 218px; height: 245px; transform: rotate(6deg); }
  .snapshot--classroom .photo { background: linear-gradient(160deg, #c7d6e2, #b8493f 55%, #e49a3c); }
  .snapshot--play { left: 765px; top: 145px; width: 262px; height: 212px; transform: rotate(-3deg); }
  .snapshot--play .photo { background: linear-gradient(135deg, #e6b7a3, #e8604f 45%, #f4a9c4); }
  .snapshot--toys { left: 772px; top: 320px; width: 292px; height: 255px; transform: rotate(7deg); }
  .snapshot--toys .photo { background: linear-gradient(150deg, #f3d0c0, #e65b63 45%, #f7c8d4); }

  .price-badge { position: absolute; left: 862px; top: 470px; width: 196px; height: 196px; z-index: 5; }
  .price-badge svg { position: absolute; inset: 0; width: 100%; height: 100%; }
  .price-badge .badge-text {
    position: absolute; inset: 0; text-align: center; padding-top: 40px;
    font-family: "Questrial", sans-serif; color: var(--navy);
  }
  .badge-only { font-family: "Jost", sans-serif; font-weight: 500; font-size: 20px; line-height: 20px; }
  .badge-price { color: var(--orange); font-family: "Jost", sans-serif; font-weight: 500; font-size: 66px; line-height: 64px; }
  .badge-price .currency { font-size: 38px; font-weight: 400; }
  .badge-label { font-size: 14px; line-height: 16px; }
</style>
</head>
<body>
  <div class="postcard">
    <div class="group-photo" role="img" aria-label="Photo of smiling children in a circle joining hands, seen from above"></div>

    <h1 class="headline">NEW <span class="accent">PEDIATRIC SPEECH THERAPY</span><br>PRACTICE IN ORINDA</h1>

    <p class="intro">Halvery Speech-Language Center, a<br>new speech therapy practice in Orinda<br>owned by Maren Halvery, MS, CCC-SLP,<br>is offering low cost ($40) on site speech-<br>language screenings at preschools this<br>Fall in the Lamorinda area.</p>

    <div class="call-block">
      <p class="call-today">Call Today!!</p>
      <p class="phone">(925) 555-0142</p>
      <p class="call-note">for additional information, or to<br>schedule an <span class="highlight">on-site screening</span><br>at your preschool today!</p>
    </div>

    <p class="website">www.halveryspeech-languagecenter.com</p>

    <div class="brand-band">
      <p class="brand-name">Halvery Speech-Language Center</p>
      <p class="brand-services">Speech, Language, and Social Communication Therapy Services</p>
    </div>

    <div class="snapshot snapshot--classroom"><div class="photo" role="img" aria-label="Photo of a teacher reading a book to preschoolers in a classroom"></div></div>
    <div class="snapshot snapshot--play"><div class="photo" role="img" aria-label="Photo of a therapist playing with a young girl at a table"></div></div>
    <div class="snapshot snapshot--toys"><div class="photo" role="img" aria-label="Photo of a therapist and a little girl playing with toys"></div></div>

    <div class="price-badge">
      <svg viewBox="0 0 200 200" aria-hidden="true">
        <circle cx="100" cy="100" r="88" fill="#fff"/>
        <circle cx="100" cy="100" r="88" fill="none" stroke="#fff" stroke-width="22" stroke-dasharray="1 22" stroke-linecap="round"/>
        <circle cx="100" cy="100" r="82" fill="var(--sun)"/>
        <circle cx="100" cy="100" r="82" fill="none" stroke="var(--sun)" stroke-width="14" stroke-dasharray="1 20.5" stroke-linecap="round"/>
      </svg>
      <div class="badge-text">
        <p class="badge-only">ONLY</p>
        <p class="badge-price">40<span class="currency">$</span></p>
        <p class="badge-label">SPEECH-LANGUAGE<br>SCREENING</p>
      </div>
    </div>
  </div>
</body>
</html>
```